Book Cover for Productivity Book

I need a book cover for my latest publication "On Momentum: The Gathered Insights of the Busiest Woman Living"

You can see my branding at www.brightmarrow.example

This is meant to be my epic pinaccle work on productivity, I want it to look like the end all be all word on productivity.

Target Market(s)

entrepreneurs

```html
<!DOCTYPE html>
<html lang="en">
<head>
<meta charset="utf-8">
<title>On Momentum — Book Cover</title>
<link href="https://fonts.googleapis.com/css2?family=Bebas+Neue&family=Lexend:wght@600&display=swap" rel="stylesheet">
<style>
  :root {
    --backdrop: #c9ccce;
    --cover-beige: #d5c9ab;
    --ink-navy: #0b1a27;
    --photo-sky: #b8c2cb;
    --photo-mist: #c7cac9;
    --photo-wood: #ddcba8;
  }
  html, body {
    margin: 0;
    padding: 0;
    width: 1200px;
    height: 1200px;
    overflow: hidden;
    background: var(--backdrop);
  }
  .book-cover {
    position: absolute;
    left: 242px;
    top: 60px;
    width: 715px;
    height: 1080px;
    background: var(--cover-beige);
    overflow: hidden;
  }
  .cover-photo {
    position: absolute;
    left: 0;
    top: 0;
    width: 715px;
    height: 540px;
    background: linear-gradient(180deg,
      var(--photo-sky) 0%,
      var(--photo-mist) 62%,
      var(--photo-wood) 86%,
      var(--cover-beige) 100%);
  }
  .cover-type {
    position: absolute;
    left: 0;
    top: 0;
    width: 715px;
    height: 1080px;
  }
  .title-line {
    font-family: "Bebas Neue", "Arial Narrow", sans-serif;
    fill: var(--ink-navy);
  }
  .subtitle {
    font-family: "Lexend", "Helvetica", sans-serif;
    font-weight: 600;
    font-size: 24px;
    fill: var(--ink-navy);
  }
</style>
</head>
<body>
  <div class="book-cover">
    <div class="cover-photo" role="img" aria-label="Photo of a hand placing a wooden block with a green upward arrow on top of a small pyramid of arrow blocks on a wooden table"></div>
    <svg class="cover-type" viewBox="0 0 715 1080" xmlns="http://www.w3.org/2000/svg">
      <text class="title-line title-on" x="302" y="591" font-size="147" textLength="114" lengthAdjust="spacingAndGlyphs">ON</text>
      <text class="title-line title-main-top" x="92" y="804" font-size="280" textLength="546" lengthAdjust="spacingAndGlyphs">MOME</text>
      <text class="title-line title-main-bottom" x="53" y="1015" font-size="305" textLength="627" lengthAdjust="spacingAndGlyphs">NTUM</text>
      <text class="subtitle" x="59" y="1049" textLength="617" lengthAdjust="spacingAndGlyphs">The Gathered Insights of the Busiest Woman Living</text>
    </svg>
  </div>
</body>
</html>
```